Velvet Crest Car Detailing Brochure

I would like a trifold brochure designed for my car detailing business. The background has to be full black or mostly black with some designing using only colors present in our logo.

Front page must have our logo and name, list of services, a photo and mybe our phone number but no long text.

Inside I want to present each service one by one with its description and a photo representing/showing each service. (I will provide the text below). For photos, use stock photos and I will add come of mines already too.

On the back of the brochure I want to have contact & info: phone number, opening hours, address, website, Instagram.

Outside left I want the text About us and photo/design.

I want the brochure to be neat, professional, easy to read, but at the same time not too boring.

Text:
1. About us
a. the ultimate destination for car care in Geneva. We provide personalized, detail-oriented services that bring out the best in your car. With our expert techniques and dedicated approach, we ensure that your car receives the utmost care and attention. Experience a place where passion meets precision and let us create an exceptional car care experience designed just for you.
2. Services:

DETAILING & HAND WASH

• Comprehensive exterior & interior care
• Personalisation and tailored cleaning packages
• Decontamination
• Premium products
• Attention to detail for a perfect finish

POLISHING

• Eliminates scratches, holograms
• Revives and protects paint
• Ensures lasting gloss
• Enhances paint life
• Preserves car’s value and beauty

CERAMIC TREATMENT

• Durable paint protection
• Water-repellent (hydrophobic) effect
• Easier cleaning, enhanced shine
• Long-term surface safeguarding
• Shields against environmental impacts

DRY ICE WASH

• Innovative, waterless method
• Safe for all car parts
• Deep cleans, removes odors
• Allergen-free, antibacterial
• Gentle, effective
• Advanced cleaning technology

COVERING

• Personalized vehicle styling
• More than 150 colours available
• Clean cut without using a cutter
• High-quality, durable materials
• Custom designs available

PROTECTION FILM

• Invisible, durable shield
• Self-healing technology
• 10-year warranty by QR VONT

DETAILING BOUTIQUE

• Premium brands available
• Buy on site during your visit
• Marble Harbour, Zeb Autos, DRUP Polaro
• Essential for at-home car care
• Perfect for quick touch-ups
(for these three brands you can put their logos

Target Market(s)

Our target market includes car owners of all price ranges, with a special focus on those who are passionate about their vehicles. We cater to clients who value excellent service and results, and seek to maintain their cars in pristine condition.

Industry/Entity Type

Automobile / Car detailing

Colors

Designer to choose colors to be used in the design.

Requirements
Must have
• Brand Consistency: The brochure must adhere to our brand colors and style, particularly utilizing the colors present in our logo. Trifold Layout: The design must be specifically tailored for a trifold brochure format. Legibility: Text must be easy to read against the mostly black background, with appropriate font size and style. Professional Look and Feel: The overall design must convey professionalism while being engaging and not overly complex. Photo representation: each service description should have a phot presenting it.
Should not have
• Overcrowded Design: Avoid cluttering with too much text or too many images. The layout should be clean and easy to navigate. Cartoonish Fonts or Graphics: Avoid using unprofessional or casual fonts and graphics that do not align with the upscale and professional image of our business. Distracting Backgrounds: The background should complement and not overpower the content. Stick to the theme of mostly black with design elements from our logo.

```html
<!DOCTYPE html>
<html lang="en">
<head>
<meta charset="utf-8">
<title>Velvet Crest Car Detailing – Trifold Brochure</title>
<link href="https://fonts.googleapis.com/css2?family=Montserrat:wght@500;700;800;900&family=Open+Sans:wght@400;600&display=swap" rel="stylesheet">
<style>
:root{
  --bg:#ececee;
  --black:#0a0a0d;
  --panel:#111116;
  --white:#ffffff;
  --grey:#c9c9d2;
  --pink:#ec3a8e;
  --magenta:#c22fd2;
  --purple:#7a3fe6;
  --blue:#3b8ff0;
  --grad:linear-gradient(90deg,var(--pink),var(--magenta) 45%,var(--purple) 75%,var(--blue));
  --grad-v:linear-gradient(160deg,var(--pink),var(--magenta) 50%,var(--purple));
}
*{box-sizing:border-box;margin:0;padding:0}
html,body{width:1200px;height:2224px;overflow:hidden;background:var(--bg)}
body{position:relative;font-family:"Open Sans",Arial,sans-serif;color:var(--white)}
.spread{position:absolute;left:40px;width:1120px;height:866px;background:var(--black);display:flex;box-shadow:0 10px 30px rgba(0,0,0,.25);overflow:hidden}
.spread--outside{top:164px}
.spread--inside{top:1194px}
.panel{position:relative;width:373.33px;height:100%;overflow:hidden}
.panel + .panel{border-left:1px solid rgba(255,255,255,.06)}
.deco{position:absolute;inset:0;width:100%;height:100%;pointer-events:none}
.photo{position:absolute;background:linear-gradient(135deg,#2a2a35,#5a5d6e 45%,#1b1b22)}
.photo--detail{background:linear-gradient(135deg,#3a3a46,#6c6e7c 50%,#1c1c24)}
.photo--wash{background:linear-gradient(135deg,#3a4a6a,#9aa6c4 40%,#5a3c7a 75%,#1a1a24)}
.photo--polish{background:linear-gradient(135deg,#3a2a20,#d08a3a 45%,#2a2a32)}
.photo--ceramic{background:linear-gradient(135deg,#1c2a44,#6a8ac0 50%,#101522)}
.photo--ice{background:linear-gradient(135deg,#d8e4f2,#7a8ea8 50%,#2a3140)}
.photo--wrap{background:linear-gradient(135deg,#5a1f5a,#c23a8a 50%,#2a1030)}
.photo--film{background:linear-gradient(135deg,#222831,#8a92a0 50%,#15171c)}
.photo--shop{background:linear-gradient(135deg,#202028,#4a4a5a 50%,#18181e)}
.h-title{font-family:"Montserrat",Arial,sans-serif;font-weight:900;text-transform:uppercase;letter-spacing:.5px}
/* about */
.about-title{position:absolute;left:34px;top:50px;font-size:34px;color:var(--white)}
.about-title span{color:var(--pink)}
.about-text{position:absolute;left:34px;top:110px;width:300px;font-size:13.5px;line-height:1.62;color:var(--grey)}
.about-photo{left:-60px;top:520px;width:330px;height:330px;border-radius:50%;border:6px solid var(--magenta)}
/* contact */
.contact-photo{left:86px;top:40px;width:200px;height:200px;border-radius:50%;border:6px solid var(--pink)}
.contact-band{position:absolute;left:0;top:268px;width:100%;height:120px;background:var(--grad-v);display:flex;align-items:center;justify-content:center;clip-path:polygon(0 12%,100% 0,100% 88%,0 100%)}
.contact-band .h-title{font-size:38px;line-height:1}
.contact-list{position:absolute;left:44px;top:420px;width:290px;list-style:none}
.contact-list li{display:flex;gap:14px;align-items:flex-start;margin-bottom:24px;font-size:14px;line-height:1.45}
.contact-list svg{flex:0 0 26px}
.contact-list strong{display:block;font-family:"Montserrat",Arial,sans-serif;font-weight:800;font-size:13px;color:var(--pink);letter-spacing:1px;text-transform:uppercase}
.web-bar{position:absolute;left:40px;right:40px;bottom:36px;height:42px;border-radius:21px;background:var(--grad);display:flex;align-items:center;justify-content:center;gap:10px;font-family:"Montserrat",Arial,sans-serif;font-weight:700;font-size:15px}
.web-bar i{width:10px;height:10px;border-radius:50%;background:var(--white)}
/* cover */
.cover-photo{left:0;top:0;width:100%;height:380px;clip-path:polygon(0 0,100% 0,100% 78%,0 100%)}
.brand{position:absolute;left:0;right:0;top:400px;display:flex;flex-direction:column;align-items:center;gap:14px}
.brand-dot{width:120px;height:120px;border-radius:50%;background:var(--white);border:5px solid var(--pink)}
.brand-name{font-family:"Montserrat",Arial,sans-serif;font-weight:800;font-size:18px;color:var(--white);letter-spacing:1px;text-transform:uppercase}
.cover-head{position:absolute;left:0;right:0;top:610px;text-align:center}
.cover-head .line1{font-size:22px;color:var(--white);line-height:1.2}
.cover-head .line2{font-size:52px;color:var(--pink);line-height:1.1}
/* inside */
.services-title{position:absolute;left:30px;top:30px;font-size:40px;z-index:2;text-shadow:0 2px 8px rgba(0,0,0,.6)}
.services-photo{left:0;top:0;width:100%;height:250px;clip-path:polygon(0 0,100% 0,100% 80%,0 100%)}
.service{position:absolute;left:26px;right:22px}
.service-head{display:inline-block;padding:6px 16px;border-radius:4px;background:var(--grad);font-family:"Montserrat",Arial,sans-serif;font-weight:800;font-size:15px;text-transform:uppercase;letter-spacing:.5px;margin-bottom:12px}
.service-body{display:flex;gap:14px;align-items:flex-start}
.service-body .photo{position:relative;flex:0 0 108px;height:108px;border-radius:50%;border:3px solid var(--magenta)}
.service ul{list-style:none;font-size:12.5px;line-height:1.5;color:var(--grey)}
.service li{position:relative;padding-left:14px;margin-bottom:2px}
.service li::before{content:"";position:absolute;left:0;top:7px;width:6px;height:6px;border-radius:50%;background:var(--pink)}
.brand-row{display:flex;gap:8px;margin-top:12px}
.brand-chip{flex:1;height:38px;border-radius:4px;background:var(--white);color:var(--black);display:flex;align-items:center;justify-content:center;font-family:"Open Sans",Arial,sans-serif;font-weight:600;font-size:11px;text-align:center}
</style>
</head>
<body>

<section class="spread spread--outside" aria-label="Brochure outside">
  <article class="panel panel--about">
    <svg class="deco" viewBox="0 0 373 866" preserveAspectRatio="none" aria-hidden="true">
      <defs><linearGradient id="gA" x1="0" y1="0" x2="1" y2="1"><stop offset="0" stop-color="#ec3a8e"/><stop offset=".5" stop-color="#c22fd2"/><stop offset="1" stop-color="#3b8ff0"/></linearGradient></defs>
      <polygon points="180,866 373,560 373,866" fill="url(#gA)"/>
      <polygon points="230,866 373,640 373,660 250,866" fill="#0a0a0d" opacity=".5"/>
      <rect x="34" y="96" width="60" height="4" fill="#ec3a8e"/>
    </svg>
    <h2 class="h-title about-title">About <span>us</span></h2>
    <p class="about-text">Velvet Crest Car Detailing is the ultimate destination for car care in Geneva. We provide personalized, detail-oriented services that bring out the best in your car. With our expert techniques and dedicated approach, we ensure that your car receives the utmost care and attention. Experience a place where passion meets precision and let us create an exceptional car care experience designed just for you.</p>
    <div class="photo photo--detail about-photo" role="img" aria-label="Photo of a detailer cleaning a car wheel rim"></div>
  </article>

  <article class="panel panel--contact">
    <svg class="deco" viewBox="0 0 373 866" preserveAspectRatio="none" aria-hidden="true">
      <polygon points="0,0 120,0 0,160" fill="#c22fd2" opacity=".85"/>
      <polygon points="373,120 373,300 260,300" fill="#3b8ff0" opacity=".6"/>
    </svg>
    <div class="photo contact-photo" role="img" aria-label="Photo of a car interior being cleaned"></div>
    <div class="contact-band"><h2 class="h-title">Contact us</h2></div>
    <ul class="contact-list">
      <li>
        <svg width="26" height="26" viewBox="0 0 24 24" aria-hidden="true"><circle cx="12" cy="12" r="12" fill="#ec3a8e"/><path d="M8.5 6.5l2 2-1.2 1.5c.7 1.6 2 2.9 3.7 3.7l1.5-1.2 2 2-1.3 1.8c-4.2-.6-7.9-4.3-8.5-8.5z" fill="#fff"/></svg>
        <span><strong>Phone</strong>+41 22 555 01 48</span>
      </li>
      <li>
        <svg width="26" height="26" viewBox="0 0 24 24" aria-hidden="true"><circle cx="12" cy="12" r="12" fill="#c22fd2"/><path d="M12 5a4.5 4.5 0 0 0-4.5 4.5c0 3.3 4.5 9 4.5 9s4.5-5.7 4.5-9A4.5 4.5 0 0 0 12 5zm0 6.2a1.7 1.7 0 1 1 0-3.4 1.7 1.7 0 0 1 0 3.4z" fill="#fff"/></svg>
        <span><strong>Address</strong>12 Rue des Lilas, 1204 Genève</span>
      </li>
      <li>
        <svg width="26" height="26" viewBox="0 0 24 24" aria-hidden="true"><circle cx="12" cy="12" r="12" fill="#7a3fe6"/><circle cx="12" cy="12" r="6" fill="none" stroke="#fff" stroke-width="1.8"/><path d="M12 8.5V12l2.5 1.5" stroke="#fff" stroke-width="1.8" fill="none"/></svg>
        <span><strong>Opening hours</strong>Mon – Sat: 8:00 – 19:00</span>
      </li>
      <li>
        <svg width="26" height="26" viewBox="0 0 24 24" aria-hidden="true"><circle cx="12" cy="12" r="12" fill="#3b8ff0"/></svg>
        <span><strong>Instagram</strong>@velvetcrest.detailing</span>
      </li>
    </ul>
    <div class="web-bar"><i></i>www.velvetcrest.ch</div>
  </article>

  <article class="panel panel--cover">
    <div class="photo photo--wash cover-photo" role="img" aria-label="Photo of a foam-covered car being hand washed"></div>
    <svg class="deco" viewBox="0 0 373 866" preserveAspectRatio="none" aria-hidden="true">
      <defs><linearGradient id="gC" x1="0" y1="0" x2="1" y2="0"><stop offset="0" stop-color="#ec3a8e"/><stop offset=".5" stop-color="#c22fd2"/><stop offset="1" stop-color="#7a3fe6"/></linearGradient></defs>
      <polygon points="0,380 373,296 373,312 0,398" fill="url(#gC)"/>
    </svg>
    <div class="brand">
      <div class="brand-dot" aria-hidden="true"></div>
      <div class="brand-name">Velvet Crest Car Detailing</div>
    </div>
    <div class="cover-head">
      <div class="h-title line1">The ultimate<br>destination for</div>
      <div class="h-title line2">Car care</div>
    </div>
    <div class="web-bar"><i></i>www.velvetcrest.ch</div>
  </article>
</section>

<section class="spread spread--inside" aria-label="Brochure inside">
  <article class="panel">
    <div class="photo photo--wash services-photo" role="img" aria-label="Photo of a car under a pressure washer"></div>
    <h2 class="h-title services-title">Services:</h2>
    <div class="service" style="top:280px">
      <h3 class="service-head">Detailing &amp; hand wash</h3>
      <div class="service-body">
        <div class="photo photo--wash" role="img" aria-label="Photo of hand washing a car"></div>
        <ul>
          <li>Comprehensive exterior &amp; interior care</li>
          <li>Personalisation and tailored cleaning packages</li>
          <li>Decontamination</li>
          <li>Premium products</li>
          <li>Attention to detail for a perfect finish</li>
        </ul>
      </div>
    </div>
    <div class="service" style="top:560px">
      <h3 class="service-head">Polishing</h3>
      <div class="service-body">
        <div class="photo photo--polish" role="img" aria-label="Photo of machine polishing car paint"></div>
        <ul>
          <li>Eliminates scratches, holograms</li>
          <li>Revives and protects paint</li>
          <li>Ensures lasting gloss</li>
          <li>Enhances paint life</li>
          <li>Preserves car’s value and beauty</li>
        </ul>
      </div>
    </div>
  </article>

  <article class="panel">
    <svg class="deco" viewBox="0 0 373 866" preserveAspectRatio="none" aria-hidden="true">
      <defs><linearGradient id="gI" x1="0" y1="0" x2="1" y2="1"><stop offset="0" stop-color="#ec3a8e"/><stop offset=".55" stop-color="#c22fd2"/><stop offset="1" stop-color="#3b8ff0"/></linearGradient></defs>
      <polygon points="0,0 373,0 373,40 0,90" fill="url(#gI)"/>
      <polygon points="0,866 373,866 373,800 0,840" fill="url(#gI)"/>
    </svg>
    <div class="service" style="top:120px">
      <h3 class="service-head">Ceramic treatment</h3>
      <div class="service-body">
        <div class="photo photo--ceramic" role="img" aria-label="Photo of water beading on a ceramic-coated bonnet"></div>
        <ul>
          <li>Durable paint protection</li>
          <li>Water-repellent (hydrophobic) effect</li>
          <li>Easier cleaning, enhanced shine</li>
          <li>Long-term surface safeguarding</li>
          <li>Shields against environmental impacts</li>
        </ul>
      </div>
    </div>
    <div class="service" style="top:440px">
      <h3 class="service-head">Dry ice wash</h3>
      <div class="service-body">
        <div class="photo photo--ice" role="img" aria-label="Photo of dry ice blasting an engine bay"></div>
        <ul>
          <li>Innovative, waterless method</li>
          <li>Safe for all car parts</li>
          <li>Deep cleans, removes odors</li>
          <li>Allergen-free, antibacterial</li>
          <li>Gentle, effective</li>
          <li>Advanced cleaning technology</li>
        </ul>
      </div>
    </div>
  </article>

  <article class="panel">
    <div class="service" style="top:36px">
      <h3 class="service-head">Covering</h3>
      <div class="service-body">
        <div class="photo photo--wrap" role="img" aria-label="Photo of a car being wrapped in coloured vinyl"></div>
        <ul>
          <li>Personalized vehicle styling</li>
          <li>More than 150 colours available</li>
          <li>Clean cut without using a cutter</li>
          <li>High-quality, durable materials</li>
          <li>Custom designs available</li>
        </ul>
      </div>
    </div>
    <div class="service" style="top:300px">
      <h3 class="service-head">Protection film</h3>
      <div class="service-body">
        <div class="photo photo--film" role="img" aria-label="Photo of clear protection film applied to a bumper"></div>
        <ul>
          <li>Invisible, durable shield</li>
          <li>Self-healing technology</li>
          <li>10-year warranty by QR VONT</li>
        </ul>
      </div>
    </div>
    <div class="service" style="top:520px">
      <h3 class="service-head">Detailing boutique</h3>
      <div class="service-body">
        <div class="photo photo--shop" role="img" aria-label="Photo of car care products on boutique shelves"></div>
        <ul>
          <li>Premium brands available</li>
          <li>Buy on site during your visit</li>
          <li>Essential for at-home car care</li>
          <li>Perfect for quick touch-ups</li>
        </ul>
      </div>
      <div class="brand-row">
        <div class="brand-chip">Marble Harbour</div>
        <div class="brand-chip">Zeb Autos</div>
        <div class="brand-chip">DRUP Polaro</div>
      </div>
    </div>
  </article>
</section>

</body>
</html>
```